Kestrel Valley Alpine Riders Society needs a business card design

We need a business card design for our newly incorporated KVARS. We are helping the NZ Chinese community, as well as everyone else, to organise ski & snowboarding trips, training, and equipments. The design should be creative, energetic, young and vibrant.

Industry/Entity Type

Social Club

Contact Information for Business Card

Logo; Kestrel Valley Alpine Riders Society; Name: Oliver Brandt; Position: President; Address: 42 Marwick Rd, Epsom, Auckland 1051; Mobile: 020 7826 1957; Email: oliver@kvars-club.example; Web: www.kvars-club.example

Requirements
Must have
• 1, The text "Kestrel Valley Alpine Riders Society" should be put together with the supplied logo file to form a new complete logo combination.
• 2, Final design files should be in Adobe Illustrator format and all text must be editable.
Nice to have
• two or three colours

```html
<!DOCTYPE html>
<html lang="en">
<head>
<meta charset="utf-8">
<title>Kestrel Valley Alpine Riders Society – Business Card</title>
<link rel="stylesheet" href="https://fonts.googleapis.com/css2?family=Roboto:wght@400;500;700&display=swap">
<style>
  :root {
    --stage: #e4e4e4;
    --navy: #03207a;
    --sky: #1fb8ef;
    --sky-deep: #1b7fd0;
    --white: #ffffff;
    --paper: #f4f4f4;
    --ink-grey: #5a5a5a;
    --logo-blue: #0a2f96;
  }
  * { box-sizing: border-box; margin: 0; padding: 0; }
  html, body {
    width: 1200px;
    height: 960px;
    overflow: hidden;
    background: var(--stage);
    font-family: "Roboto", Arial, sans-serif;
  }
  .card {
    position: absolute;
    width: 602px;
    height: 343px;
    overflow: hidden;
  }
  .card--front {
    left: 314px;
    top: 113px;
    background: var(--navy);
  }
  .card--back {
    left: 311px;
    top: 472px;
    width: 600px;
    background: var(--paper);
  }
  .front__art {
    position: absolute;
    right: 0;
    top: 0;
    width: 330px;
    height: 100%;
    background: linear-gradient(160deg, var(--sky) 0%, var(--sky-deep) 100%);
    clip-path: polygon(30% 0, 100% 0, 100% 100%, 0 100%, 8% 55%, 0 20%);
  }
  .contact {
    position: absolute;
    left: 47px;
    top: 133px;
    color: var(--white);
  }
  .contact__name {
    font-size: 20px;
    font-weight: 500;
    color: var(--sky);
    line-height: 24px;
    text-transform: uppercase;
  }
  .contact__role {
    font-size: 15px;
    font-weight: 500;
    line-height: 20px;
    text-transform: uppercase;
  }
  .contact__address {
    margin-top: 20px;
    font-size: 14px;
    line-height: 18px;
  }
  .contact__list {
    list-style: none;
    margin-top: 11px;
    font-size: 14px;
    line-height: 19.5px;
  }
  .contact__list li {
    display: flex;
    align-items: center;
    gap: 6px;
  }
  .contact__icon {
    width: 13px;
    height: 13px;
    flex: none;
  }
  .brand {
    position: absolute;
    left: 0;
    right: 0;
    top: 106px;
    text-align: center;
    color: var(--logo-blue);
  }
  .brand__short {
    font-size: 66px;
    font-weight: 700;
    line-height: 80px;
  }
  .brand__full {
    margin-top: 4px;
    font-size: 14px;
    font-weight: 700;
    line-height: 18px;
    letter-spacing: 0.04em;
    text-transform: uppercase;
  }
  .brand__url {
    position: absolute;
    left: 0;
    right: 0;
    top: 293px;
    text-align: center;
    font-size: 13px;
    letter-spacing: 0.45em;
    color: var(--ink-grey);
  }
</style>
</head>
<body>
  <section class="card card--front" aria-label="Business card front">
    <div class="front__art" role="img" aria-label="Illustration of a snowboarder mid-jump in light blue tones"></div>
    <div class="contact">
      <p class="contact__name">Oliver Brandt</p>
      <p class="contact__role">President</p>
      <p class="contact__address">42 Marwick Rd, Epsom<br>Auckland 1051</p>
      <ul class="contact__list">
        <li>
          <svg class="contact__icon" viewBox="0 0 13 13" aria-hidden="true"><rect x="3" y="0.5" width="7" height="12" rx="1.3" fill="none" stroke="#1fb8ef" stroke-width="1.3"/><rect x="4.5" y="2.2" width="4" height="7" fill="#1fb8ef"/></svg>
          020 7826 1957
        </li>
        <li>
          <svg class="contact__icon" viewBox="0 0 13 13" aria-hidden="true"><rect x="0.5" y="3" width="12" height="8" fill="#1fb8ef"/><path d="M0.5 3 L6.5 7.5 L12.5 3" fill="none" stroke="#03207a" stroke-width="1"/></svg>
          oliver@kvars-club.example
        </li>
        <li>
          <svg class="contact__icon" viewBox="0 0 13 13" aria-hidden="true"><circle cx="6.5" cy="6.5" r="6" fill="#1fb8ef"/><path d="M3 4 Q5 3 6 5 T9 9 M8 2.5 Q9.5 4 10.5 4" fill="none" stroke="#03207a" stroke-width="1.1"/></svg>
          www.kvars-club.example
        </li>
      </ul>
    </div>
  </section>

  <section class="card card--back" aria-label="Business card back">
    <div class="brand">
      <p class="brand__short">KVARS</p>
      <p class="brand__full">Kestrel Valley Alpine Riders Society</p>
    </div>
    <p class="brand__url">www.kvars-club.example</p>
  </section>
</body>
</html>
```